" Modo tradicional de funcionamento de drogarias, com diversas seções de produtos, mas evidentemente tendo como principal produto a comercialização de medicamentos. "

```html
<!DOCTYPE html>
<html lang="pt-BR">
<head>
<meta charset="utf-8">
<title>Crachá PharmaVila</title>
<link href="https://fonts.googleapis.com/css2?family=Montserrat:wght@500;700;800&display=swap" rel="stylesheet">
<style>
  :root {
    --backdrop: #8f8f8f;
    --card-white: #ffffff;
    --sky: #7cb8e2;
    --sky-deep: #6aaedc;
    --teal: #22a39a;
    --text-white: #ffffff;
    --slot: #9a9a9a;
    --photo-top: #c9c9c9;
    --photo-bottom: #3a3f48;
  }
  * { margin: 0; padding: 0; box-sizing: border-box; }
  html, body { width: 1200px; height: 1200px; overflow: hidden; }
  body {
    background: var(--backdrop);
    font-family: "Montserrat", sans-serif;
    position: relative;
  }
  .badge {
    position: absolute;
    top: 348px;
    width: 336px;
    height: 504px;
    border-radius: 26px;
    overflow: hidden;
    box-shadow: 0 3px 10px rgba(0,0,0,0.25);
  }
  .badge--front { left: 247px; background: var(--card-white); }
  .badge--back { left: 622px; background: var(--sky); }
  .badge__slot {
    position: absolute;
    top: 22px; left: 50%;
    transform: translateX(-50%);
    width: 108px; height: 29px;
    border-radius: 15px;
    background: var(--slot);
  }
  .brand {
    position: absolute;
    left: 0; right: 0;
    display: flex;
    align-items: center;
    justify-content: center;
    gap: 10px;
    font-weight: 800;
  }
  .brand__dot { border-radius: 50%; flex: none; }
  .badge--front .brand { top: 80px; color: var(--teal); font-size: 36px; }
  .badge--front .brand__dot { width: 30px; height: 30px; background: var(--teal); }
  .badge--back .brand { top: 382px; color: var(--text-white); font-size: 26px; }
  .badge--back .brand__dot { width: 22px; height: 22px; background: var(--text-white); }
  .portrait {
    position: absolute;
    top: 139px; left: 96px;
    width: 140px; height: 183px;
    background: linear-gradient(180deg, var(--photo-top) 0%, var(--photo-bottom) 100%);
  }
  .holder-name {
    position: absolute;
    top: 346px; left: 0; right: 0;
    text-align: center;
    color: var(--sky-deep);
    font-weight: 700;
    font-size: 34px;
  }
  .holder-role {
    position: absolute;
    top: 388px; left: 0; right: 0;
    text-align: center;
    color: var(--teal);
    font-weight: 500;
    font-size: 13px;
    letter-spacing: 4px;
  }
  .wave { position: absolute; left: 0; bottom: 0; width: 336px; height: 100px; }
  .field { position: absolute; left: 36px; width: 266px; }
  .field__label {
    color: var(--text-white);
    font-weight: 700;
    font-size: 19px;
    margin-bottom: 6px;
  }
  .field__box {
    height: 27px;
    border: 2px solid var(--text-white);
    border-radius: 14px;
  }
  .field--name { top: 98px; }
  .field--id { top: 190px; }
  .field--code { top: 276px; }
</style>
</head>
<body>
  <section class="badge badge--front">
    <div class="badge__slot"></div>
    <div class="brand"><span class="brand__dot"></span>PharmaVila</div>
    <div class="portrait" role="img" aria-label="Foto do colaborador"></div>
    <div class="holder-name">Nome Sobrenome</div>
    <div class="holder-role">CARGO | FUNÇÃO</div>
    <svg class="wave" viewBox="0 0 336 100" preserveAspectRatio="none">
      <path d="M0 62 C90 22 150 92 232 56 S318 22 336 26 L336 100 L0 100 Z" fill="var(--sky)"/>
      <path d="M0 62 C90 22 150 92 232 56 S318 22 336 26" fill="none" stroke="var(--teal)" stroke-width="5"/>
    </svg>
  </section>

  <section class="badge badge--back">
    <div class="badge__slot"></div>
    <div class="field field--name"><div class="field__label">Nome Sobrenome:</div><div class="field__box"></div></div>
    <div class="field field--id"><div class="field__label">Identidade:</div><div class="field__box"></div></div>
    <div class="field field--code"><div class="field__label">Código:</div><div class="field__box"></div></div>
    <div class="brand"><span class="brand__dot"></span>PharmaVila</div>
    <svg class="wave" viewBox="0 0 336 100" preserveAspectRatio="none">
      <path d="M0 46 C80 20 140 96 232 70 S318 30 336 40 L336 100 L0 100 Z" fill="var(--card-white)"/>
      <path d="M0 46 C80 20 140 96 232 70 S318 30 336 40" fill="none" stroke="var(--teal)" stroke-width="5"/>
    </svg>
  </section>
</body>
</html>
```